Business Card - high end, modern health care

Hey designers!

We need a double sided business card for the boutique, cutting edge physical therapy rehabilitation centre in Sydney's Northern Beaches.

With the most qualified physios in the area The Harbourline Motion Clinic does what other physiotherapy practices do not, we take our time with our patients giving them longer appointments, better physios and therefor faster results!

We guarantee that the service people receive at THMC will be unparalleled.

Hence we need a business card to reflect our modern, boutique, high end service. The final design needs to reflect that we are in a class of our own yet with the feel of beachside retreat.

Below I have attached our logo in both blue on white and white on blue. The exact colour is;
and the font that we have used in our logo is Tex Gyre Aventador.

I like the idea of the blue as the main colour as it is more eye catching and our signage onto the main road will be in this blue and in the interest of consistency across marketing the blue needs to be a part of the design. However I would appreciate a few designs onto a wooden background as this is a visual theme within the fitout of the practice.

The design needs to be of standard size (91x55mm).

Target Market(s)

We target people who have an end outcome in mind and those who have had poor experiences with other providers and ensure that everyone gets the care that they deserve with a premium service that is tailored to the individuals circumstances. As a premium service, the target market is highly educated, business and tech savvy with the additional target market of elderly people who have self funded their retirement and see value in paying for the best ongoing rehabilitation to maintain independence.

Industry/Entity Type

Physical Therapy

Contact Information for Business Card

Name, designation( Titled Musculoskeletal Physiotherapist... there will also be those in the company that have multiple designations ie 5 or 6 words long), phone number, email, facebook, instagram, address

Font styles to use
Sans Serif

Colors

Designer to choose colors to be used in the design.

Requirements
Must have
• Front - The logo as large as possible, blue or wooden theme, and all of the important details.
• Back - A blank space/lines on which to write appointment times (no "Appointment, date, time" etc.)
Nice to have
• facebook url
• logos for facebook and instagram
• Mini logos for the phone and email?

```html
<!DOCTYPE html>
<html lang="en">
<head>
<meta charset="UTF-8">
<title>The Harbourline Motion Clinic – Business Card</title>
<link rel="stylesheet" href="https://fonts.googleapis.com/css2?family=Montserrat:wght@400;500;600;700&display=swap">
<style>
  :root{
    --brand-blue:#0f56a8;
    --card-white:#ffffff;
    --ink:#3a3a3a;
    --rule:#8a8a8a;
    --backdrop:#4a4540;
  }
  *{box-sizing:border-box;margin:0;padding:0}
  html,body{width:1200px;height:930px;overflow:hidden}
  body{background:var(--backdrop);font-family:"Montserrat",sans-serif;position:relative}

  .card{position:absolute;width:620px;height:375px;background:var(--card-white);border-radius:16px;overflow:hidden;box-shadow:0 10px 26px rgba(0,0,0,.35)}

  /* logo lockup */
  .logo{display:flex;align-items:center;gap:12px;font-weight:700}
  .logo__dot{width:44px;height:44px;border-radius:50%;flex:none}
  .logo__text{display:flex;flex-direction:column;line-height:1}
  .logo__name{font-size:30px;letter-spacing:-.5px}
  .logo__sub{font-size:16px;letter-spacing:6.5px;margin-top:4px}

  /* back */
  .card--back{left:70px;top:55px}
  .back__band{position:absolute;left:0;top:0;width:100%;height:170px;background:var(--brand-blue);display:flex;justify-content:center;align-items:center}
  .back__band .logo{color:var(--card-white)}
  .back__band .logo__dot{background:var(--card-white)}
  .back__label{position:absolute;top:186px;width:100%;text-align:center;color:var(--brand-blue);font-size:15px;font-weight:500;letter-spacing:.5px}
  .back__lines{position:absolute;left:60px;right:60px;top:232px}
  .back__line{height:1px;background:var(--rule);margin-bottom:42px}

  /* front */
  .card--front{left:510px;top:500px}
  .front__logo{position:absolute;left:38px;top:56px;color:var(--brand-blue)}
  .front__logo .logo__dot{background:var(--brand-blue)}
  .front__tab{position:absolute;right:0;top:86px;width:26px;height:36px;background:var(--brand-blue)}
  .front__person{position:absolute;right:44px;top:82px;text-align:right}
  .front__name{color:var(--brand-blue);font-size:27px;font-weight:600;letter-spacing:-.3px;text-transform:uppercase}
  .front__role{color:var(--ink);font-size:15px;margin-top:2px}
  .front__rule{position:absolute;left:120px;right:34px;top:168px;height:2px;background:var(--brand-blue)}
  .front__address{position:absolute;right:44px;top:184px;text-align:right;color:var(--ink);font-size:15px;line-height:1.45}
  .front__contacts{position:absolute;left:40px;top:222px;list-style:none;color:var(--ink);font-size:16px}
  .front__contacts li{display:flex;align-items:center;gap:10px;margin-bottom:6px}
  .front__contacts svg{width:14px;height:14px;flex:none}
  .front__contacts .accent{color:var(--brand-blue)}
  .front__wave{position:absolute;left:0;bottom:0;width:620px;height:140px}
</style>
</head>
<body>

<section class="card card--back" aria-label="Back of card">
  <div class="back__band">
    <div class="logo">
      <span class="logo__dot"></span>
      <span class="logo__text">
        <span class="logo__name">THE HARBOURLINE</span>
        <span class="logo__sub">MOTION CLINIC</span>
      </span>
    </div>
  </div>
  <p class="back__label">Appointment</p>
  <div class="back__lines">
    <div class="back__line"></div>
    <div class="back__line"></div>
    <div class="back__line"></div>
  </div>
</section>

<section class="card card--front" aria-label="Front of card">
  <div class="logo front__logo">
    <span class="logo__dot"></span>
    <span class="logo__text">
      <span class="logo__name">THE HARBOURLINE</span>
      <span class="logo__sub">MOTION CLINIC</span>
    </span>
  </div>

  <div class="front__tab"></div>
  <div class="front__person">
    <p class="front__name">Daniel Reyes</p>
    <p class="front__role">Director</p>
  </div>
  <div class="front__rule"></div>
  <p class="front__address">27 Pittwater Road, Unit 4,<br>Manly, NSW 2095</p>

  <ul class="front__contacts">
    <li>
      <svg viewBox="0 0 16 16" aria-hidden="true"><path fill="#0f56a8" d="M3.5 1.5l2.5 0 1 3.5-1.6 1.2a9 9 0 0 0 4.4 4.4L11 9l3.5 1v2.5c0 1-1 2-2 2C6.5 14.5 1.5 9.5 1.5 3.5c0-1 1-2 2-2z"/></svg>
      <span>+330 5812-4470</span>
    </li>
    <li>
      <svg viewBox="0 0 16 16" aria-hidden="true"><rect x="1.5" y="3.5" width="13" height="9" rx="1" fill="none" stroke="#0f56a8" stroke-width="1.6"/><path d="M2 4l6 5 6-5" fill="none" stroke="#0f56a8" stroke-width="1.6"/></svg>
      <span>info@harbourline.com</span>
    </li>
    <li>
      <svg viewBox="0 0 16 16" aria-hidden="true"><circle cx="8" cy="8" r="6.5" fill="none" stroke="#0f56a8" stroke-width="1.4"/><ellipse cx="8" cy="8" rx="2.8" ry="6.5" fill="none" stroke="#0f56a8" stroke-width="1.2"/><path d="M1.5 8h13" stroke="#0f56a8" stroke-width="1.2"/></svg>
      <span>www.<span class="accent">harbourline</span>.com</span>
    </li>
  </ul>

  <svg class="front__wave" viewBox="0 0 620 140" preserveAspectRatio="none" aria-hidden="true">
    <path d="M0 140 L0 118 C150 112 260 100 360 60 C450 22 540 6 620 4 L620 140 Z" fill="#0f56a8"/>
    <path d="M0 112 C160 106 270 88 365 46 C455 8 545 -2 620 0" fill="none" stroke="#0f56a8" stroke-width="2.5"/>
  </svg>
</section>

</body>
</html>
```